Plakate für Psychologische Beratung am Telefon
Zielgruppe
Psychologische Beratung am Telefon
Aufgabenstellung
anliegendes Word Dokument soll als eine Art 'Plakat' (pdf Datei) erstellt werden. Diese PDF Datei wird dann an alle MitarbeiterInnen gesandt und soll Auskunft über das Beratungsangebot geben. Die Farben bitte so wie auf dieser Website (das ist unser Mutterunternehmen). www.lindenhof-kolleg.com.

```html
<!DOCTYPE html>
<html lang="de">
<head>
<meta charset="utf-8">
<title>Beratungs-Telefon – Lindenhof Kolleg</title>
<link rel="stylesheet" href="https://fonts.googleapis.com/css2?family=Open+Sans:wght@400;600;700;800&display=swap">
<style>
  :root {
    --brand-blue: #42679e;
    --ink: #222222;
    --paper: #f4f4f6;
    --footer-grey: #ececee;
    --panel: rgba(255,255,255,0.82);
    --white: #ffffff;
  }
  * { box-sizing: border-box; margin: 0; padding: 0; }
  html, body { width: 811px; height: 1200px; overflow: hidden; }
  body { font-family: "Open Sans", Arial, sans-serif; color: var(--ink); background: var(--paper); }
  .poster { position: relative; width: 811px; height: 1200px; background: var(--paper); overflow: hidden; }

  .brand { position: absolute; left: 470px; top: 48px; display: flex; align-items: center; gap: 12px; }
  .brand-square { width: 26px; height: 26px; background: var(--ink); }
  .brand-name { font-weight: 600; font-size: 20px; letter-spacing: 2px; color: var(--ink); }

  .headline { position: absolute; left: 46px; top: 126px; font-size: 32px; line-height: 43px; text-transform: uppercase; color: var(--ink); }
  .headline .light { font-weight: 400; display: block; }
  .headline .strong { font-weight: 800; display: block; }

  .rule-band { position: absolute; left: 0; top: 326px; width: 811px; height: 9px; background: var(--brand-blue); }

  .photo { position: absolute; left: 0; top: 335px; width: 811px; height: 726px;
    background: linear-gradient(90deg, #eef0f3 0%, #e6e9ee 40%, #d9c8bd 62%, #f1ece8 80%, #e9ebee 100%); }

  .hotline { position: absolute; left: 0; top: 335px; width: 399px; height: 212px; background: var(--brand-blue); color: var(--white); padding: 20px 0 0 35px; }
  .hotline p { font-weight: 700; font-size: 15.5px; line-height: 29px; }
  .hotline .phone { font-size: 27px; font-weight: 800; line-height: 38px; }
  .hotline .hours { font-weight: 400; font-size: 15.5px; }

  .spine { position: absolute; left: 75px; top: 547px; width: 9px; height: 613px; background: var(--brand-blue); }

  .panel { position: absolute; left: 84px; top: 642px; width: 702px; height: 403px; background: var(--panel); }

  .tab { position: absolute; left: 84px; background: var(--brand-blue); color: var(--white); font-weight: 800; font-size: 31px; padding-left: 14px; line-height: 1; display: flex; align-items: center; }
  .tab-who { top: 588px; width: 204px; height: 54px; }
  .tab-fields { top: 684px; width: 407px; height: 55px; }
  .tab-process { top: 884px; width: 232px; height: 47px; }

  .who-text { position: absolute; left: 100px; top: 650px; font-size: 13.5px; }

  .field { position: absolute; top: 745px; font-size: 13.5px; line-height: 20.5px; }
  .field h3 { font-size: 13.5px; font-weight: 700; }
  .field-private { left: 100px; width: 215px; }
  .field-health { left: 319px; width: 200px; }
  .field-work { left: 522px; width: 262px; }

  .process { position: absolute; left: 104px; top: 942px; font-size: 13.5px; line-height: 20.5px; }
  .process h3 { font-size: 16px; font-weight: 700; line-height: 22px; }
  .process ul { list-style: none; }
  .process li { position: relative; padding-left: 25px; }
  .process li::before { content: "•"; position: absolute; left: 0; }

  .footer { position: absolute; left: 0; top: 1061px; width: 811px; height: 139px; background: var(--footer-grey); }
  .privacy { position: absolute; left: 104px; top: 1076px; font-size: 13.5px; line-height: 20px; font-weight: 600; }
  .privacy .label { font-weight: 600; }
</style>
</head>
<body>
<main class="poster">
  <div class="brand">
    <span class="brand-square"></span>
    <span class="brand-name">LINDENHOF KOLLEG</span>
  </div>

  <h1 class="headline">
    <span class="light">Das anonyme</span>
    <span class="strong">Beratungs- und Begleitangebot</span>
    <span class="strong">für Mitarbeiterinnen &amp; Führungskräfte</span>
    <span class="light">in schwierigen Berufs- und Lebensphasen.</span>
  </h1>

  <div class="rule-band"></div>
  <div class="photo" role="img" aria-label="Foto einer Beraterin mit Headset am Telefon, heller Büro-Hintergrund"></div>

  <section class="hotline">
    <p>Das LHK Beratungs-Telefon der LHK<br>Lindenhof Kolleg für Hochschulbildung.</p>
    <p class="phone">Tel.: 0451 – 555 20 – 140</p>
    <p>Sofortberatung oder Terminvereinbarung<br>zu Ihrer Wunschzeit</p>
    <p class="hours">Di. 14:00 – 17:00 Uhr &amp; Do. 9:00 – 12:00 Uhr</p>
  </section>

  <div class="spine"></div>
  <div class="panel"></div>

  <h2 class="tab tab-who">FÜR WEN?</h2>
  <p class="who-text">Für alle Mitarbeitenden und Führungskräfte der LK|FH.</p>

  <h2 class="tab tab-fields">DIE BERATUNGSFELDER</h2>
  <div class="field field-private">
    <h3>Private Anliegen:</h3>
    <p>Partnerschaftskonflikte,<br>Erziehungsberatung,<br>Trennung/Scheidung, Verlust,<br>Trauer, Todesfall,<br>Schockdiagnosen usw.</p>
  </div>
  <div class="field field-health">
    <h3>Psychische Gesundheit:</h3>
    <p>Sucht und Abhängigkeiten,<br>Depressionen, Burnout,<br>Ängste usw.</p>
  </div>
  <div class="field field-work">
    <h3>Berufliche Anliegen:</h3>
    <p>Vereinbarkeit Beruf und Familie,<br>Konflikte mit Kolleginnen oder<br>Kollegen oder Vorgesetzten,<br>Überforderungen am Arbeitsplatz<br>sowie Coaching für Führungskräfte</p>
  </div>

  <h2 class="tab tab-process">DER ABLAUF</h2>
  <div class="process">
    <h3>Sie wählen 0451 555 20 140</h3>
    <ul>
      <li>Ihr Anruf wird von den psychologischen Assistentinnen angenommen</li>
      <li>Diese erfragen ein Stichwort zu Ihrem Anliegen, um Sie</li>
      <li>direkt mit einer Expertin oder einem Experten für Ihr Thema verbinden zu können</li>
    </ul>
  </div>

  <div class="footer"></div>
  <div class="privacy">
    <p class="label">Anonymität</p>
    <p>Die Beratung ist anonym. Sie müssen Ihren Namen nicht nennen.<br>Unsere Beraterinnen und Berater verfügen alle über langjährige Beratungserfahrung<br>und je nach Thema auch über eine Psychotherapiezulassung.</p>
  </div>
</main>
</body>
</html>
```